Etiketten für Gummibärchenglas
Zielgruppe
Wir sind Arbeitgeber für Pflegeberufe und bieten Arbeitsmodelle, die den Pflegeberuf erträglicher gestalten die Mitarbeiter entlasten und besser bezahlen!
Aufgabenstellung
Unseren Bewerbern sagen wir immer....'bevor Sie sich entscheiden hören Sie auf Ihr Bauchgefühl...! ' Wenn dieses komische Signale sendet, lassen Sie lieber die Finger davon!'
Nun haben wir uns überlegt, unseren Bewerbern zum Abschied aus dem Vorstellungsgespräch ein kleines 'Einmachglas' als Geschenk mitzugeben wo nur grüne Gummibärchen darin sind und ein super ansprechenden Etikett darauf ist mit einem Satz wie z.B.: K7-VITANOR....für ein gutes Bauchgefühl.
Dieses Etikett soll selbstverständlich optisch hochwertig, witzig oder ansprechend sein. Idealerweise alles zusammen! ;)
Unsere Logos/Farben und sonstiges finden Sie unter www.dienstwerk-9.de oder auf unserer Facebook-Seite: https://www.sozialnetz-beispiel.de/DienstwerkNeun/?ref=bookmarks
hier sind die Gläser die etikettiert werden sollen: https://www.kaufhafen-online.de/dp/X00Q41ZTRA/ref=kh_5172093_296851202_QX_item

```html
<!DOCTYPE html>
<html lang="de">
<head>
<meta charset="utf-8">
<title>Etikett – Für ein gutes Bauchgefühl</title>
<link rel="stylesheet" href="https://fonts.googleapis.com/css2?family=Playfair+Display:wght@700;800&display=swap">
<style>
  :root {
    --brand-green: #13994a;
    --soft-green: #cfe9d6;
    --pale-green: #e6f4ea;
    --mid-green: #9fd6b0;
    --label-white: #ffffff;
    --backdrop: #f1f2f1;
  }
  html, body {
    margin: 0;
    padding: 0;
    width: 1200px;
    height: 1200px;
    overflow: hidden;
    background: var(--backdrop);
  }
  .canvas {
    position: relative;
    width: 1200px;
    height: 1200px;
  }
  .label {
    position: absolute;
    left: 100px;
    top: 100px;
    width: 1000px;
    height: 1000px;
    background: var(--label-white);
    box-shadow: 0 2px 10px rgba(0,0,0,0.08);
    overflow: hidden;
  }
  .label__headline {
    position: absolute;
    left: 42px;
    top: 262px;
    margin: 0;
    font-family: "Playfair Display", Georgia, serif;
    font-weight: 800;
    font-size: 122px;
    line-height: 154px;
    letter-spacing: -1px;
    color: var(--brand-green);
    z-index: 2;
  }
  .label__art {
    position: absolute;
    left: 0;
    top: 0;
    width: 1000px;
    height: 1000px;
    z-index: 1;
  }
  .brand-mark__name {
    font-family: "Playfair Display", Georgia, serif;
    font-weight: 800;
    font-size: 40px;
    fill: var(--brand-green);
  }
</style>
</head>
<body>
  <div class="canvas">
    <section class="label">
      <svg class="label__art" viewBox="0 0 1000 1000">
        <defs>
          <linearGradient id="figure-fill" x1="0" y1="0" x2="0" y2="1">
            <stop offset="0" stop-color="var(--mid-green)" stop-opacity="0.55"/>
            <stop offset="0.5" stop-color="var(--mid-green)" stop-opacity="0.75"/>
            <stop offset="1" stop-color="var(--soft-green)" stop-opacity="0.6"/>
          </linearGradient>
        </defs>
        <circle class="backdrop-circle" cx="745" cy="625" r="255" fill="var(--soft-green)"/>
        <rect class="figure-area" x="600" y="0" width="380" height="1000" rx="150"
              fill="url(#figure-fill)" role="img"
              aria-label="Illustration: junge Frau mit langen Haaren in grünem Top und Shorts, die Hände zufrieden auf dem Bauch"/>
        <g class="brand-mark">
          <circle cx="620" cy="580" r="16" fill="var(--brand-green)"/>
          <text class="brand-mark__name" x="648" y="594">K7-VITANOR</text>
        </g>
      </svg>
      <h1 class="label__headline">Für ein<br>gutes<br>Bauch-<br>gefühl.</h1>
    </section>
  </div>
</body>
</html>
```